Business card design for new brand

We have recently rebranded and need a new business card template.

We are an insurance underwriting agency. All of our products are sold via other partner companies, so these are just to pass on our details to other organisations.

We would like to see designs that use the colour green (current stationary generally uses lime green (rgb 142,190,63) and forest green (0,154,79) to comply with our logo's colours. We are happy with other shades of green.

Business cards need to include our logo, as well as space for:
1. Full name
2. Qualifications (optional)
3. Title
4. Office number
5. Mobile number
6. Email address

Our logo is enclosed here.

```html
<!DOCTYPE html>
<html lang="en">
<head>
<meta charset="utf-8">
<title>Verdant Cover – Business Card</title>
<link rel="stylesheet" href="https://fonts.googleapis.com/css2?family=Open+Sans:wght@400;600&family=Arimo:wght@400;700&display=swap">
<style>
  :root {
    --lime: #8ebe3f;
    --forest: #009a4f;
    --ink: #1a1a1a;
    --card-white: #ffffff;
    --card-black: #1c1c1c;
    --brand-on-black: #5a5a5a;
    --bg-top: #d2d2d2;
    --bg-bottom: #a4a4a4;
  }
  * { margin: 0; padding: 0; box-sizing: border-box; }
  html, body { width: 1200px; height: 788px; overflow: hidden; }
  body {
    background: linear-gradient(180deg, var(--bg-top), var(--bg-bottom));
    font-family: "Arimo", Arial, sans-serif;
    color: var(--ink);
    position: relative;
  }
  .card {
    position: absolute;
    top: 246px;
    width: 520px;
    height: 297px;
    box-shadow: 0 10px 24px rgba(0,0,0,0.25);
  }
  .card-front { left: 70px; background: var(--card-white); }
  .card-back { left: 610px; background: var(--card-black); }

  .brand {
    display: flex;
    align-items: center;
    gap: 12px;
    font-family: "Open Sans", sans-serif;
    font-weight: 600;
  }
  .brand-square { display: block; flex: none; background: var(--forest); }

  .card-front .brand { position: absolute; left: 34px; top: 34px; }
  .card-front .brand-square { width: 30px; height: 30px; }
  .card-front .brand-name { font-size: 26px; color: var(--ink); letter-spacing: 0.2px; }

  .accent-bar {
    position: absolute; left: 0; top: 118px;
    width: 12px; height: 40px; background: var(--forest);
  }
  .person { position: absolute; left: 34px; top: 110px; }
  .person-name {
    font-weight: 700; font-size: 24px; color: var(--lime);
    letter-spacing: 0.3px; line-height: 1.1;
  }
  .person-title { font-size: 14px; margin-top: 3px; }

  .address { position: absolute; left: 34px; top: 178px; font-size: 13px; line-height: 1.35; }
  .contacts { position: absolute; left: 34px; top: 224px; list-style: none; font-size: 13px; line-height: 1.35; }
  .contacts li { display: flex; align-items: center; gap: 6px; }
  .contacts svg { width: 11px; height: 11px; flex: none; }

  .card-back .brand {
    position: absolute; left: 0; right: 0; top: 50%;
    transform: translateY(-50%); justify-content: center; gap: 16px;
  }
  .card-back .brand-square { width: 42px; height: 42px; }
  .card-back .brand-name { font-size: 30px; color: var(--brand-on-black); }
</style>
</head>
<body>
  <section class="card card-front" aria-label="Business card front">
    <div class="brand">
      <span class="brand-square"></span>
      <span class="brand-name">Verdant Cover Pty Ltd</span>
    </div>
    <span class="accent-bar"></span>
    <div class="person">
      <p class="person-name">DANIEL HART</p>
      <p class="person-title">Director/Founder</p>
    </div>
    <p class="address">820 B. Linden Street<br>Harbor, CD 31907</p>
    <ul class="contacts">
      <li>
        <svg viewBox="0 0 12 12" aria-label="Office phone"><path d="M3 1 L5 3.5 L4 4.8 C4.7 6.3 5.7 7.3 7.2 8 L8.5 7 L11 9 L9.8 11 C5.5 10.6 1.4 6.5 1 2.2 Z" fill="var(--forest)"/></svg>
        <span>555.210.4417</span>
      </li>
      <li>
        <svg viewBox="0 0 12 12" aria-label="Mobile"><rect x="3" y="0.8" width="6" height="10.4" rx="1" fill="none" stroke="var(--forest)" stroke-width="1.4"/><circle cx="6" cy="9.2" r="0.7" fill="var(--forest)"/></svg>
        <span>555.683.9032</span>
      </li>
      <li>
        <svg viewBox="0 0 12 12" aria-label="Email"><rect x="0.7" y="2.2" width="10.6" height="7.6" fill="var(--forest)"/><path d="M0.7 2.2 L6 6.4 L11.3 2.2" fill="none" stroke="#fff" stroke-width="1"/></svg>
        <span>hello@verdantcover.com</span>
      </li>
    </ul>
  </section>

  <section class="card card-back" aria-label="Business card back">
    <div class="brand">
      <span class="brand-square"></span>
      <span class="brand-name">Verdant Cover Pty Ltd</span>
    </div>
  </section>
</body>
</html>
```